Vantor Grid Advisory Partners - Website

Design & Build a website for a new company which operates in the Systems and Technology space for Transportation, Government and Commercial sectors.

Overall design should be minimalist in nature.
Should also have a feed that provides news and event updates on the main page.
Logo has already been awarded and should be incorporated into the site.

We like the overall layout, functionality and simplicity of the below sites. Submitted designs could be similar to or a combination of the aspects on these sites, or perhaps a whole different concept - we are open to new ideas.
Morqeli.com
Tumb.it

All I am moving away from the Tumb.it website and would like it to be more aligned with Morqeli.com not only in layout but in functionality. I will be extending the deadline of this design brief for two weeks to incorporate additional requirements and will add addtional funding to the project.

Apologies for not having more information available to provide but with so many submissions its getting confusing.

Thanks Dorian

Important: We will need two language versions of the website, English and Arabic; the website is hosted on HostPivo

Hello All, Thank you for your submissions. We have narrowed it down to the final 6 designers and I just wanted to take a moment and provide a bit of feedback regarding the concepts that we like and the modifications we are looking for. First, let me mention some of the design functions we like. - At the top of the homepage we really like the "region" or "language" tab so that the website can be viewed in both English and Arabic. - We like the homepage to have clear color variation so that the different sections of the homepage are distinct. Additionally, we like the bottom portion of the homepage to be in red. We feel that draws attention to our contact information. Again, we would like the colors to integrate black, gray-scale, red, etc. - Having a search tab at the top of the home page, or integrated into the main image, so that the site is easy to navigate. - We especially like the main image to have the scrolling tabs at the bottom so it is easy to browse the services offered (Consultancy, Solutions Architecture, Masters Systems Integration, Independent Design Review). - In regards to the services offered tab we really like the idea that a few people presented that have the outside of our logo with an icon in the middle of consultancy, solutions, etc., etc. Secondly, as mentioned in our brief we really enjoy the design of morqeli site. Specially, we enjoy the strong iconic images they use, the way the tabs at the top scroll easily, and contact us page that generates an email. Lastly, I've included some photos of the concept we have been working on. What we are trying to demonstrate is how our company offers a range of services that are essentially linked together. We provide individual services that when combined present the full service package. We would like this concept to be integrated into the over concept of our website. Please feel free to ask for clarification of any of the above points or contact us if you have any additional questions. We appreciate all of your hard work and are very excited to see the updated designs. Best, Miriam Okaford Vangridex Senior Program Manager miriam.okaford@vangridax.example

Industry/Entity Type

Government

Font styles to use
Serif
Sans Serif

Requirements
Must have
• Must work on/adapt to various/mobile devices (responsive)
Must be simple and straightforward
Colors should be in line/matching with logo
2 language versions: English and Arabic (no Thai)
Services should be the first group/row of items after/below the main image
Note: the website will be hosted by hostpivo
Nice to have
• Submit feedback form
What's New section
The banner at the bottom of the site should not be too large; we would like a narrow one more
It would be nice if the header/top banner (with Home, About, etc. tabs) could stay in place as you scroll down (like Morqeli and Chatterly)
We will likely only use one image with a Company slogan on the Home page rather than a carousel of images to rotate through
Should not have
• This is the existing website: http://www.vangridex.example
We do not like the animation, the way the banner icons/titles bounce
Not simple enough, we don't like the functionality or how pages load so slowly
We do not like the logo centered - it should be at the left
The banner and its tabs should not be towards the right, we would like them to be centered, to go all the way across and to be below the logo

```html
<!DOCTYPE html>
<html lang="en">
<head>
<meta charset="utf-8">
<title>Vangridex – Home</title>
<link href="https://fonts.googleapis.com/css2?family=Raleway:wght@300;400;500;600&family=Open+Sans:wght@400;600&display=swap" rel="stylesheet">
<style>
:root{
  --red:#d7212b;
  --red-dark:#b01821;
  --ink:#333333;
  --text:#6a6a6a;
  --muted:#9a9a9a;
  --line:#d6d6d6;
  --paper:#ffffff;
  --mist:#f2f2f2;
  --band:#e6e6e6;
  --night:#1c1c1c;
}
*{margin:0;padding:0;box-sizing:border-box}
html,body{width:1200px;height:2552px;overflow:hidden;background:var(--paper)}
body{position:relative;font-family:"Open Sans",Arial,sans-serif;color:var(--text)}
.abs{position:absolute}
.heading{font-family:"Raleway",Arial,sans-serif}

/* header */
.site-header{left:0;top:0;width:1200px;height:60px;background:var(--paper);z-index:3}
.nav{top:0;height:60px;display:flex;gap:34px;align-items:center;font-family:"Raleway",sans-serif;font-size:12px;font-weight:500;letter-spacing:.6px;color:#777}
.nav-left{left:150px}
.nav-right{right:150px}
.nav a{color:inherit;text-decoration:none;position:relative}
.nav a.active{color:var(--red)}
.nav a.active::after{content:"";position:absolute;left:0;right:0;bottom:-8px;height:2px;background:var(--red)}
.lang{right:60px;top:2px;background:#8c8c8c;color:#fff;font-size:10px;padding:2px 18px 2px 8px}
.lang::after{content:"";position:absolute;right:6px;top:7px;border:3px solid transparent;border-top-color:#fff}
.brand-tab{left:555px;top:0;width:90px;height:76px;background:var(--red);display:flex;align-items:center;justify-content:center;z-index:4}
.brand-name{font-family:"Raleway",sans-serif;font-weight:600;font-size:13px;letter-spacing:1.5px;color:#fff}

/* hero */
.hero{left:0;top:60px;width:1200px;height:340px;background:linear-gradient(100deg,#3a3a3a 0%,#6d6d6d 35%,#555 60%,#2a2a2a 100%)}
.hero-title{left:215px;top:238px;width:800px;font-family:"Raleway",sans-serif;font-weight:400;font-size:40px;line-height:50px;color:#fff;letter-spacing:.5px}

/* intro */
.intro-mark{left:580px;top:642px;width:40px;height:40px;border:6px solid var(--red)}
.intro{left:180px;top:730px;width:840px;text-align:center;font-size:13px;line-height:21px;color:var(--text)}
.intro p{margin-bottom:18px}
.section-title{left:0;width:1200px;display:flex;align-items:center;justify-content:center;gap:18px;font-family:"Raleway",sans-serif;font-weight:400;font-size:24px;letter-spacing:1px;color:var(--ink)}
.section-title::before,.section-title::after{content:"";width:150px;height:1px;background:var(--line)}

/* updates */
.updates{left:0;top:1160px;width:1200px;height:500px;background:var(--mist)}
.update-head{font-family:"Raleway",sans-serif;font-weight:400;font-size:26px;color:var(--red)}
.update-text{font-size:13px;color:var(--ink)}
.update-text a{color:var(--red);text-decoration:none;font-weight:600}
.media{background:linear-gradient(135deg,#cfcfcf,#8a8a8a)}

/* services */
.services{left:0;top:1660px;width:1200px;height:390px;background:var(--band)}
.service{top:1800px;width:110px;text-align:center}
.service-icon{width:64px;height:64px;margin:0 auto;border:3px solid #a4a4a4;border-radius:50%;display:flex;align-items:center;justify-content:center}
.service-icon svg{width:30px;height:30px;stroke:#a4a4a4;fill:none;stroke-width:2}
.service-label{margin-top:14px;font-family:"Raleway",sans-serif;font-size:10px;font-weight:600;letter-spacing:.6px;color:var(--muted)}
.service.active .service-icon{border-color:var(--red)}
.service.active svg{stroke:var(--red)}
.service.active .service-label{color:var(--red)}

/* footer */
.footer{left:0;top:2050px;width:1200px;height:410px;background:var(--red)}
.f-col{top:2110px;width:280px;color:#fff;font-size:12px;line-height:20px}
.f-head{font-family:"Raleway",sans-serif;font-weight:600;font-size:13px;letter-spacing:.8px;margin-bottom:16px}
.f-row{display:flex;align-items:center;gap:10px;margin-bottom:8px}
.f-dot{width:22px;height:22px;border-radius:50%;background:rgba(255,255,255,.22);display:flex;align-items:center;justify-content:center}
.f-dot svg{width:12px;height:12px;fill:#fff}
.f-news p{margin-bottom:14px}
.skyline{left:0;top:2390px;width:1200px;height:70px;background:linear-gradient(180deg,var(--red) 0%,var(--red-dark) 100%)}
.bottom-bar{left:0;top:2460px;width:1200px;height:92px;background:var(--night)}
.legal{left:150px;top:2490px;display:flex;gap:18px;font-size:10px;color:#aaa}
.copy{left:150px;top:2516px;font-size:10px;color:#777}
.foot-brand{left:970px;top:2478px;width:80px;height:56px;background:var(--red);display:flex;align-items:center;justify-content:center}
</style>
</head>
<body>

<header class="abs site-header">
  <nav class="abs nav nav-left"><a class="active">HOME</a><a>BUSINESS UNITS</a><a>SERVICES</a></nav>
  <nav class="abs nav nav-right"><a>ABOUT US</a><a>LOCATIONS</a><a>CONTACT US</a></nav>
  <div class="abs lang">English</div>
</header>
<div class="abs brand-tab"><span class="brand-name">VANGRIDEX</span></div>

<section class="abs hero" role="img" aria-label="Photograph of an engineer working in a server room, in greyscale"></section>
<h1 class="abs hero-title">DELIVERING QUALITY PROFESSIONAL SERVICES AND TECHNICAL PROJECTS</h1>

<div class="abs intro-mark"></div>
<div class="abs intro">
  <p>Vangridex specializes in delivering quality professional services and technical projects that support larger business goals. systems are tools that support a greater business function and need. we understand that most technical projects are conceptualized to support a larger vision with actual business goals in mind and ensure that all of our professional and certified expertise is included in our professional services to meet those goals.</p>
  <p>Vangridex recognizes the middle east and greater asia regions are economic growth markets with developing infrastructure projects requiring specialist systems and technical expertise. accordingly, Vangridex has evolved its presence in the regions to meet client demands and expectations.</p>
  <p>our ultimate goal is to provide quality, technical and professional services on projects of any scale and/or complexity, from conception through to completion. our philosophy is simple: stick to what you are good at and be the best at it.</p>
</div>
<h2 class="abs section-title" style="top:1096px">MEET OUR EXPERIENCES</h2>

<section class="abs updates"></section>
<h3 class="abs update-head" style="left:150px;top:1284px">WHAT'S NEW</h3>
<div class="abs media" style="left:150px;top:1340px;width:420px;height:270px" role="img" aria-label="Phone and laptop showing the website with a data centre banner"></div>
<h3 class="abs update-head" style="left:668px;top:1284px">NEWS &amp; EVENTS</h3>
<p class="abs update-text" style="left:668px;top:1334px">Lorem ipsum dolor sit amet consecutor... <a>READ MORE</a></p>
<div class="abs media" style="left:668px;top:1380px;width:380px;height:225px;background:linear-gradient(135deg,#e2e2e2,#777)" role="img" aria-label="Photograph of an airport departure board"></div>

<section class="abs services"></section>
<h2 class="abs section-title" style="top:1716px">SERVICES WE OFFER</h2>

<div class="abs service" style="left:160px"><div class="service-icon"><svg viewBox="0 0 30 30"><rect x="4" y="6" width="22" height="14"/><path d="M11 25h8M15 20v5"/></svg></div><div class="service-label">IT CONSULTING</div></div>
<div class="abs service" style="left:285px"><div class="service-icon"><svg viewBox="0 0 30 30"><rect x="7" y="4" width="16" height="20" rx="2"/><path d="M7 16h16M10 27v-3M20 27v-3"/></svg></div><div class="service-label">BUS SYSTEMS</div></div>
<div class="abs service" style="left:410px"><div class="service-icon"><svg viewBox="0 0 30 30"><path d="M15 3v24M5 17l10-5 10 5M11 26l4-2 4 2"/></svg></div><div class="service-label">AVIATION</div></div>
<div class="abs service active" style="left:535px"><div class="service-icon"><svg viewBox="0 0 30 30"><circle cx="15" cy="15" r="10"/><path d="M5 15h20M15 5c-4 4-4 16 0 20M15 5c4 4 4 16 0 20"/></svg></div><div class="service-label">WEBSITE DESIGN</div></div>
<div class="abs service" style="left:660px"><div class="service-icon"><svg viewBox="0 0 30 30"><path d="M6 20l10-10M12 6l8 8M5 26h14"/></svg></div><div class="service-label">GOVERNMENT</div></div>
<div class="abs service" style="left:785px"><div class="service-icon"><svg viewBox="0 0 30 30"><path d="M4 11h22l-3 13H7zM10 11l5-7 5 7"/></svg></div><div class="service-label">COMMERCIAL</div></div>
<div class="abs service" style="left:910px"><div class="service-icon"><svg viewBox="0 0 30 30"><path d="M4 12a16 16 0 0 1 22 0M8 17a10 10 0 0 1 14 0M12 22a4 4 0 0 1 6 0"/></svg></div><div class="service-label">NETWORKS</div></div>
<div class="abs service" style="left:1035px;width:90px"><div class="service-icon"><svg viewBox="0 0 30 30"><circle cx="15" cy="11" r="5"/><path d="M6 26c1-6 17-6 18 0"/></svg></div><div class="service-label">SUPPORT</div></div>

<footer class="abs footer"></footer>
<div class="abs f-col" style="left:150px">
  <div class="f-head">MAIN OFFICE</div>
  <p>14 Cedar Row, Harlan District<br>Tower B, Floor 6, Suite 12</p>
  <div role="img" aria-label="Street map of the office location" style="margin-top:14px;width:210px;height:100px;background:linear-gradient(135deg,#f3e9dc,#d9d2c4)"></div>
</div>
<div class="abs f-col" style="left:470px">
  <div class="f-head">GET IN TOUCH</div>
  <div class="f-row"><span class="f-dot"><svg viewBox="0 0 12 12"><path d="M2 1h3l1 3-2 1a7 7 0 0 0 3 3l1-2 3 1v3c-6 0-9-3-9-9z"/></svg></span>+000 120 458 2291</div>
  <div class="f-row"><span class="f-dot"><svg viewBox="0 0 12 12"><path d="M1 3h10v6H1zM1 3l5 4 5-4" fill="none" stroke="#fff"/></svg></span>info@vangridex.example</div>
  <div style="height:18px"></div>
  <div class="f-row"><span class="f-dot"></span>Like Us On Chatterly</div>
  <div class="f-row"><span class="f-dot"></span>Follow Us On Chirpwell</div>
  <div class="f-row"><span class="f-dot"></span>Find Us On Linkora</div>
</div>
<div class="abs f-col f-news" style="left:790px">
  <div class="f-head">NEWS AND EVENTS</div>
  <p>Lorem ipsum dolor sit amet consecutor<br>Lorem ipsum dolor</p>
  <p>Lorem ipsum dolor sit amet consecutor<br>Lorem ipsum dolor</p>
  <p>Lorem ipsum dolor sit amet consecutor<br>Lorem ipsum dolor</p>
  <p>Lorem ipsum dolor sit amet consecutor<br>Lorem ipsum dolor</p>
</div>
<div class="abs skyline" role="img" aria-label="City skyline silhouette along the bottom of the footer"></div>

<div class="abs bottom-bar"></div>
<div class="abs legal"><span>Privacy Policy</span><span>Disclaimer</span><span>Terms &amp; Conditions</span></div>
<div class="abs copy">© 2015 Vangridex</div>
<div class="abs foot-brand"><span class="brand-name" style="font-size:11px">VANGRIDEX</span></div>

</body>
</html>
```